Harbor Fieldworks (Business Card Design)

Need business cards designed. Something modern, chic, and sleek. Mabye the back of the card should be the navy blue that is in the logo and then just the logo on the back.

Target Market(s)

Those in the hotel, office, and renovation industry

Contact Information for Business Card

1. Logo 2. Dorian Velasko 3. CEO/Founder 4. Phone: (833) HarbFld / (833) 427-2353 5. Email: dorian@theharborfieldworks.com 6. Website: www.theharborfieldworks.com

Font styles to use
Other font styles liked:
• Look at the logo font and base the font for everything else off of that.

Colors
0054AA
0677BA
7BADD7
CADEEF
E8F1F8

Requirements
Must have
• Colors that are associated in the logo
Nice to have
• Sleek modern clean and chic design.

```html
<!DOCTYPE html>
<html lang="en">
<head>
<meta charset="utf-8">
<title>Harbor Fieldworks — Business Card</title>
<link rel="stylesheet" href="https://fonts.googleapis.com/css2?family=Montserrat:wght@500;600&family=Poppins:wght@400&family=Raleway:wght@700&display=swap">
<style>
  :root {
    --backdrop: #8b8b8b;
    --navy: #0b1942;
    --gold: #cca74e;
    --white: #ffffff;
  }
  * { box-sizing: border-box; margin: 0; padding: 0; }
  html, body {
    width: 1093px;
    height: 1200px;
    overflow: hidden;
    background: var(--backdrop);
  }
  .sheet { position: relative; width: 1093px; height: 1200px; }
  .card {
    position: absolute;
    left: 265px;
    width: 580px;
    height: 356px;
    border-radius: 28px;
    background: var(--navy);
    overflow: hidden;
  }
  .card--front { top: 226px; }
  .card--back { top: 621px; }

  .accent-panel { position: absolute; inset: 0; width: 100%; height: 100%; }

  .identity { position: absolute; left: 26px; top: 48px; }
  .identity__name {
    font-family: "Raleway", sans-serif;
    font-weight: 700;
    font-size: 23px;
    line-height: 1;
    color: var(--white);
  }
  .identity__role {
    font-family: "Poppins", sans-serif;
    font-size: 14px;
    line-height: 1.3;
    margin-top: 2px;
    color: var(--gold);
  }

  .contact { position: absolute; left: 26px; top: 243px; list-style: none; }
  .contact__item {
    display: flex;
    align-items: center;
    height: 24.5px;
    font-family: "Poppins", sans-serif;
    font-size: 17px;
    color: var(--white);
    white-space: nowrap;
  }
  .contact__icon { width: 16px; height: 16px; margin-right: 7px; flex: none; }

  .brand {
    position: absolute;
    left: 0;
    right: 0;
    top: 120px;
    display: flex;
    flex-direction: column;
    align-items: center;
  }
  .brand__mark { width: 14px; height: 14px; background: var(--gold); margin-bottom: 30px; }
  .brand__name {
    font-family: "Montserrat", sans-serif;
    font-weight: 600;
    font-size: 25px;
    letter-spacing: 3px;
    color: var(--white);
  }
</style>
</head>
<body>
<main class="sheet">
  <section class="card card--front" aria-label="Card front">
    <svg class="accent-panel" viewBox="0 0 580 356" aria-hidden="true">
      <polygon points="449,0 580,0 580,356 449,356 272,177" fill="var(--gold)"/>
    </svg>

    <header class="identity">
      <h1 class="identity__name">DORIAN VELASKO</h1>
      <p class="identity__role">CEO/FOUNDER</p>
    </header>

    <ul class="contact">
      <li class="contact__item">
        <svg class="contact__icon" viewBox="0 0 16 16" aria-hidden="true">
          <path d="M4 1.5l2.2 3-1.3 1.5c.8 1.9 2.2 3.3 4.1 4.1l1.5-1.3 3 2.2-1.2 2.5C6.8 13.2 2.8 9.2 1.5 3.2z" fill="none" stroke="var(--gold)" stroke-width="1.6" stroke-linejoin="round"/>
          <path d="M9.5 2.5a4 4 0 0 1 4 4M9.5 5a1.5 1.5 0 0 1 1.5 1.5" fill="none" stroke="var(--gold)" stroke-width="1.4" stroke-linecap="round"/>
        </svg>
        (833) HarbFld / (833) 427-2353
      </li>
      <li class="contact__item">
        <svg class="contact__icon" viewBox="0 0 16 16" aria-hidden="true">
          <rect x="0.5" y="3" width="15" height="10" fill="var(--gold)"/>
          <path d="M0.5 3l7.5 6 7.5-6M0.5 13l5.5-5M15.5 13l-5.5-5" fill="none" stroke="var(--navy)" stroke-width="1.1"/>
        </svg>
        dorian@theharborfieldworks.com
      </li>
      <li class="contact__item">
        <svg class="contact__icon" viewBox="0 0 16 16" aria-hidden="true">
          <g fill="none" stroke="var(--gold)" stroke-width="1.3">
            <circle cx="8" cy="8" r="6.8"/>
            <ellipse cx="8" cy="8" rx="3" ry="6.8"/>
            <path d="M1.2 8h13.6M2.2 4.6h11.6M2.2 11.4h11.6M8 1.2v13.6"/>
          </g>
        </svg>
        www.theharborfieldworks.com
      </li>
    </ul>
  </section>

  <section class="card card--back" aria-label="Card back">
    <div class="brand">
      <span class="brand__mark" aria-hidden="true"></span>
      <p class="brand__name">HARBOR FIELDWORKS</p>
    </div>
  </section>
</main>
</body>
</html>
```